Landing Page for Martial Arts School

We'd like our page to look very much like http://www.moveonpinegrove.example/. I've attached our text and you can see how I've tried to make it similar to their site in placement.
We'd like to do a darker green instead of their blue shading, obviously our logo (the dragon image) instead of theirs, our student photo or a better image you may choose, and instead of a solid block of text under "Welcome . . ." we'd like the USA Badge to the right of the text. At the bottom of the page we'd like a big button with our phone number. I know this is a lot to take in, but we're so looking forward to seeing your designs!

These designs are looking good! I'm sending each of you a few suggested tweaks for now! Best of luck!

As we enter the final few days of competition, I'd like to give a final word of thanks to all of our designers. We have moved out of good and into excellent, and we thank you all. We've also updated the student image we'd like you to use. All of the remaining designers will need to update their photos with the new one, please. Also, if you've one of the final designs, I'll be sending you a final set of notes and then we will be selecting someone. We may push back the final selection until Monday, depending.

Reason: We're going to discuss the finalized versions of your designs on Monday and make our final selection. If for some reason, none of the designers have made our suggested tweaks, then we still have another day.

```html
<!DOCTYPE html>
<html lang="en">
<head>
<meta charset="utf-8">
<title>Ridgeline TaeKwonDo</title>
<link rel="stylesheet" href="https://fonts.googleapis.com/css2?family=PT+Sans:wght@400;700&family=Arimo:wght@400;700&display=swap">
<style>
:root{
  --green:#2c7410;
  --green-dark:#256a0c;
  --title-green:#2a6e0a;
  --black:#000;
  --ink:#222;
  --white:#fff;
  --rule:#b5b5b5;
  --footer-text:#8a8a8a;
}
*{margin:0;padding:0;box-sizing:border-box}
html,body{width:758px;height:1200px;overflow:hidden;background:var(--white)}
.page{position:relative;width:758px;height:1200px;font-family:"Arimo",Arial,sans-serif;color:var(--ink)}
.abs{position:absolute}

.header-rule{left:0;top:74px;width:758px;height:3px;background:var(--black)}
.nav-band{left:0;top:78px;width:758px;height:30px;background:var(--green)}
.nav-item{top:78px;height:30px;line-height:30px;font-size:9.5px;color:var(--white);text-align:center;text-transform:uppercase}
.nav-item.active{background:var(--black)}
.nav-divider{top:84px;width:1px;height:18px;background:#5d9a45}

.brand{left:72px;top:6px;width:94px;height:94px;border-radius:50%;background:var(--white);border:3px solid var(--black);display:flex;align-items:center;justify-content:center;text-align:center;font-family:"PT Sans",sans-serif;font-weight:700;font-size:15px;line-height:1.1;color:var(--black)}

.call{display:flex;align-items:center;background:linear-gradient(#2a2a2a,#000);border:2px solid var(--black);box-shadow:0 0 0 1.5px var(--white),0 0 0 3px var(--black);border-radius:5px;color:var(--white)}
.call svg{flex:none}
.call .label{font-size:15px;margin:0 5px 0 7px}
.call .number{font-weight:700;font-size:22px;letter-spacing:.3px}
.call-top{left:421px;top:18px;width:268px;height:38px;padding-left:12px}
.call-mid{left:250px;top:378px;width:301px;height:47px;padding-left:10px}
.call-mid .label{font-size:16px}
.call-mid .number{font-size:26px}

.photo{top:108px;height:246px}
.photo-a{left:0;width:232px;background:linear-gradient(160deg,#d9d6cf 0%,#5a5650 45%,#1f4fa0 85%,#2358b0 100%)}
.photo-b{left:232px;width:294px;background:linear-gradient(180deg,#eae6dc 0%,#cfc7b8 40%,#2a2724 65%,#8a7a64 100%)}
.photo-c{left:526px;width:232px;background:linear-gradient(170deg,#e9e2cf 0%,#b98a5e 45%,#6b4a30 75%,#1d1a18 100%)}
.caption{left:400px;top:294px;width:344px;height:50px;background:rgba(0,0,0,.72);color:var(--white);font-family:"PT Sans",sans-serif;font-size:17px;line-height:23px;text-align:right;padding:3px 10px 0 0}
.caption b{display:block;margin-right:38px}

.rule{left:66px;width:622px;height:0;border-top:1px dotted var(--rule)}
.welcome-title{left:0;top:466px;width:758px;text-align:center;font-family:"PT Sans",sans-serif;font-size:23px;color:var(--title-green)}
.welcome-copy{left:64px;top:511px;width:630px;text-align:center;font-size:9.6px;line-height:13.7px;color:var(--ink)}
.welcome-copy .gap{height:13.7px}

.level{left:65px;height:57px;background:var(--green);color:var(--white);font-family:"PT Sans",sans-serif;font-size:28px;line-height:57px;padding-left:11px;white-space:nowrap}
.level small{font-size:15px}
.level-copy{font-size:9.8px;line-height:13.9px;color:var(--ink);text-align:justify}

.contact-band{left:0;top:955px;width:758px;height:151px;background:var(--green)}
.contact-title{left:0;top:966px;width:758px;text-align:center;font-family:"PT Sans",sans-serif;font-size:20px;color:var(--white)}
.call-big{left:250px;top:1003px;width:298px;height:69px;border-radius:4px;overflow:hidden;display:flex;background:linear-gradient(#2c2c2c,#0c0c0c)}
.call-big .icon{width:53px;height:69px;background:linear-gradient(#f2f2f2,#a9a9a9);display:flex;align-items:center;justify-content:center}
.call-big .text{color:var(--white);font-family:"PT Sans",sans-serif;font-size:19px;line-height:69px;padding-left:11px;white-space:nowrap}
.call-big .text b{font-size:23px}

.footer{left:0;top:1106px;width:758px;height:94px;background:var(--black)}
.footer-address{left:68px;top:1130px;font-family:"PT Sans",sans-serif;font-size:11px;color:var(--footer-text)}
.footer-copy{left:69px;top:1154px;font-size:8px;color:var(--footer-text)}
.badge{left:617px;top:1120px;width:64px;height:64px;border-radius:50%;background:#d6d6d6;border:2px solid #777}
</style>
</head>
<body>
<div class="page">

  <header>
    <div class="abs header-rule"></div>
    <nav>
      <div class="abs nav-band"></div>
      <div class="abs nav-item active" style="left:418px;width:60px">About Us</div>
      <div class="abs nav-divider" style="left:498px"></div>
      <div class="abs nav-item" style="left:505px;width:88px">Classes</div>
      <div class="abs nav-divider" style="left:594px"></div>
      <div class="abs nav-item" style="left:603px;width:112px">Contact Us</div>
    </nav>
    <div class="abs brand">Ridgeline<br>TKD</div>
    <a class="abs call call-top">
      <svg width="20" height="20" viewBox="0 0 24 24" aria-hidden="true"><path fill="#fff" d="M6.6 10.8a15.1 15.1 0 0 0 6.6 6.6l2.2-2.2a1 1 0 0 1 1-.25 11.4 11.4 0 0 0 3.6.57 1 1 0 0 1 1 1V20a1 1 0 0 1-1 1A17 17 0 0 1 3 4a1 1 0 0 1 1-1h3.5a1 1 0 0 1 1 1c0 1.25.2 2.45.57 3.57a1 1 0 0 1-.25 1z"/></svg>
      <span class="label">Call Now:</span><span class="number">555.014.2280</span>
    </a>
  </header>

  <section class="hero">
    <div class="abs photo photo-a" role="img" aria-label="Instructor holding a board while a young student in a yellow belt practises a strike"></div>
    <div class="abs photo photo-b" role="img" aria-label="Row of young students in black uniforms and coloured belts standing in the dojo"></div>
    <div class="abs photo photo-c" role="img" aria-label="Smiling young student in uniform"></div>
    <div class="abs caption"><b>Dedicated Masters &amp; Instructors</b>teach students from age Three to Fourteen.</div>
  </section>

  <a class="abs call call-mid">
    <svg width="24" height="24" viewBox="0 0 24 24" aria-hidden="true"><path fill="#fff" d="M6.6 10.8a15.1 15.1 0 0 0 6.6 6.6l2.2-2.2a1 1 0 0 1 1-.25 11.4 11.4 0 0 0 3.6.57 1 1 0 0 1 1 1V20a1 1 0 0 1-1 1A17 17 0 0 1 3 4a1 1 0 0 1 1-1h3.5a1 1 0 0 1 1 1c0 1.25.2 2.45.57 3.57a1 1 0 0 1-.25 1z"/></svg>
    <span class="label">Call Now:</span><span class="number">555.014.2280</span>
  </a>

  <div class="abs rule" style="top:450px"></div>

  <section class="welcome">
    <h1 class="abs welcome-title" style="font-weight:400">Welcome to Ridgeline TaeKwonDo!</h1>
    <div class="abs welcome-copy">
      <p>Are you interested in Ridgeline TaeKwonDo classes, lessons, sparring, training, or one-on-one private tutoring in the martial arts? We are a full time martial arts academy based in Alderton, TN. We offer a range of TaeKwonDo, or Korean Karate, classes for all skill levels, but we specialize in TaeKwonDo for kids and teens!</p>
      <p>TaeKwonDo training is in a safe, friendly school under the car of an instructor with 20 years of experience in martial arts. Our Instructor, Dana Kirby, was voted 2014's Children's Instructor of the Year by the National Youth Martial Arts Council! Learn with the best!</p>
      <div class="gap"></div>
      <p><b>We are located at 48 W. Main Street right in Downtown, Alderton, TN.</b></p>
      <p>One block East of Hollis's Restaurant, across the street from Fine Arts Alder, Two Doors Down from Marlow Blues Club, and directly between Delphine's on Main and StillWater Yoga.</p>
    </div>
  </section>

  <div class="abs rule" style="top:666px"></div>

  <section class="classes">
    <div class="abs level" style="top:691px;width:230px">Beginners <small>(ages 3-7)</small></div>
    <p class="abs level-copy" style="left:311px;top:702px;width:360px;text-align:left">It is a fun, energetic introduction to the art. Students begin to learn forms. This class accepts young students.</p>

    <div class="abs level" style="top:776px;width:258px">Intermediate <small>(ages 6-15)</small></div>
    <p class="abs level-copy" style="left:333px;top:784px;width:350px">Children learn martial arts, respect, and self-defense in a safe environment. This class is based on experience level and accepts students with some experience in the art.</p>

    <div class="abs level" style="top:862px;width:216px">Advanced <small>(ages 8-14)</small></div>
    <p class="abs level-copy" style="left:294px;top:869px;width:391px">For students who have some experience past the basic level. We cover more advanced topics, higher-kicks and more sparring. We prep our students for the challenges of confrontation, bullying, and self-defense.</p>
  </section>

  <section class="contact">
    <div class="abs contact-band"></div>
    <h2 class="abs contact-title" style="font-weight:400">We’d Love to Hear From You!</h2>
    <a class="abs call-big">
      <span class="icon">
        <svg width="44" height="44" viewBox="0 0 44 44" aria-hidden="true"><circle cx="22" cy="22" r="19" fill="none" stroke="#111" stroke-width="3"/><path fill="#111" transform="translate(11 11) scale(.92)" d="M6.6 10.8a15.1 15.1 0 0 0 6.6 6.6l2.2-2.2a1 1 0 0 1 1-.25 11.4 11.4 0 0 0 3.6.57 1 1 0 0 1 1 1V20a1 1 0 0 1-1 1A17 17 0 0 1 3 4a1 1 0 0 1 1-1h3.5a1 1 0 0 1 1 1c0 1.25.2 2.45.57 3.57a1 1 0 0 1-.25 1z"/></svg>
      </span>
      <span class="text">Call Now : <b>555.014.2280</b></span>
    </a>
  </section>

  <footer>
    <div class="abs footer"></div>
    <p class="abs footer-address">We are located at 48 W. Main Street right in Downtown, Alderton, TN.</p>
    <p class="abs footer-copy">Copyright © 2014 ridgelinetkd.example All Rights Reserved.</p>
    <div class="abs badge" role="img" aria-label="Award badge"></div>
  </footer>

</div>
</body>
</html>
```